Business Card Design

I need a Business Card that will catch the attention that will not get thrown in a Drawer. I have 23 companies I use for Auto, Home, Life, and Business Insurance. I make sure that people have the best coverage for the $ spent.

Industry/Entity Type

Business

Contact Information for Business Card

Dorlin Insurance Agency, Inc., Marcus Helgren, 4375 West Tamber Lane Corvell Falls, Norland 45192 555-281-7496, www.dorlinagency.example, Facebook, LinkedIn, Google+

```html
<!DOCTYPE html>
<html lang="en">
<head>
<meta charset="utf-8">
<title>Dorlin Insurance Agency – Business Card</title>
<link href="https://fonts.googleapis.com/css2?family=Lato:wght@400;700&display=swap" rel="stylesheet">
<style>
  :root {
    --ink: #0b0b0b;
    --paper: #f7f7f5;
    --accent: #ee5125;
    --backdrop: #d9d9d9;
    --soft-white: #ffffff;
    --tile: #5a5a5a;
  }
  * { box-sizing: border-box; margin: 0; padding: 0; }
  html, body { width: 1200px; height: 1000px; overflow: hidden; }
  body {
    background: var(--backdrop);
    font-family: "Lato", sans-serif;
    position: relative;
  }
  .card {
    position: absolute;
    left: 280px;
    width: 640px;
    height: 366px;
    box-shadow: 0 10px 24px rgba(0,0,0,.25);
    overflow: hidden;
  }
  /* Front */
  .card-front { top: 90px; background: var(--ink); display: flex; align-items: center; justify-content: center; }
  .brand { display: flex; flex-direction: column; align-items: center; gap: 18px; }
  .brand-mark { width: 56px; height: 56px; background: var(--accent); }
  .brand-name {
    color: var(--soft-white);
    font-weight: 700;
    font-size: 26px;
    letter-spacing: 1px;
    line-height: 1.25;
    text-align: center;
    text-transform: uppercase;
  }
  /* Back */
  .card-back { top: 540px; background: var(--ink); display: flex; }
  .back-identity {
    width: 46%;
    background: var(--paper);
    display: flex;
    align-items: center;
    justify-content: center;
    padding: 0 24px 30px;
  }
  .back-identity .brand { gap: 14px; }
  .back-identity .brand-mark { width: 44px; height: 44px; }
  .back-identity .brand-name { color: var(--ink); font-size: 19px; }
  .back-details { flex: 1; padding: 32px 30px 40px 34px; color: var(--soft-white); display: flex; flex-direction: column; }
  .person-name { color: var(--accent); font-weight: 700; font-size: 24px; letter-spacing: 1px; text-transform: uppercase; margin-bottom: 22px; }
  .contact-line { font-size: 17px; line-height: 1.3; }
  .contact-label { color: var(--accent); font-weight: 700; }
  .address { margin-top: 34px; font-size: 17px; line-height: 1.35; }
  .address-company { color: var(--accent); font-weight: 700; }
  .social { margin-top: auto; display: flex; align-items: center; gap: 12px; }
  .social-label { color: var(--accent); font-weight: 700; font-size: 19px; margin-right: 14px; }
  .social-tile { width: 30px; height: 30px; background: var(--tile); }
  .accent-band { position: absolute; left: 0; right: 0; bottom: 0; height: 16px; background: var(--accent); }
</style>
</head>
<body>
  <section class="card card-front" aria-label="Card front">
    <div class="brand">
      <span class="brand-mark"></span>
      <span class="brand-name">Dorlin<br>Insurance Agency, Inc.</span>
    </div>
  </section>

  <section class="card card-back" aria-label="Card back">
    <div class="back-identity">
      <div class="brand">
        <span class="brand-mark"></span>
        <span class="brand-name">Dorlin<br>Insurance Agency, Inc.</span>
      </div>
    </div>
    <div class="back-details">
      <h1 class="person-name">Marcus Helgren</h1>
      <p class="contact-line"><span class="contact-label">Phone:</span> 555-630-2184 (Office)</p>
      <p class="contact-line"><span class="contact-label">Toll Free:</span> 877-555-0192</p>
      <p class="contact-line"><span class="contact-label">Fax:</span> 40-555-8813</p>
      <p class="address">
        <span class="address-company">DORLIN Insurance Agency, Inc.</span><br>
        4375 West Tamber Lane<br>
        Corvell Falls, Norland 45192
      </p>
      <div class="social">
        <span class="social-label">Join us on:</span>
        <span class="social-tile"></span>
        <span class="social-tile"></span>
        <span class="social-tile"></span>
      </div>
    </div>
    <div class="accent-band"></div>
  </section>
</body>
</html>
```